Word template Letterhead for Australian Law Firm

We are a small law firm based in Manly, NSW, Australia. We have had a new logo designed for us and wish to freshen up the appearance of our letterhead. We require the letterhead to be in a word document that we can type over. This will not be a ‘printed’ letterhead because we send the majority of our correspondence via email. We would like to see a few options. We have attached our previous letterhead as well as the artwork for our new logo. We like the idea of a watermark across the bottom of the letter but the watermark must stay in place and we must be able to type over it. We are open to some colour throughout the letterhead because the majority of our correspondence is sent electronically. We also use electronic signatures. I have uploaded an example of this.The letterhead must include:-1. Our address details – including our phone number, physical address, website address etc. These details can be found on the copy of our previous letterhead;2. ABN Number;3. The words ‘Corvenda (NSW) Pty Ltd ACN 742 185 903 trading as Shipton & AssociatesLiability limited by a scheme approved under Professional Standards Legislation. The letterhead does not need to include the names and qualifications of the people working at the firm. Thank you.

Target Market(s)

Clients and other parties

Industry/Entity Type

Law Firm

Font styles to use
Other font styles liked:
• raleway, montserrat

Colors

Designer to choose colors to be used in the design.

Requirements
Must have
• Certain wording - please see project description.
• Must be a word document and must be able to type over the watermark etc.
Nice to have
• Watermark at the bottom of the letter.

```html
<!DOCTYPE html>
<html lang="en">
<head>
<meta charset="utf-8">
<title>Ferrow &amp; Associates – Letterhead</title>
<link href="https://fonts.googleapis.com/css2?family=Montserrat:ital,wght@0,400;0,500;0,700;1,400;1,500&display=swap" rel="stylesheet">
<style>
  :root {
    --backdrop: #d5dbec;
    --paper: #ffffff;
    --brand-blue: #4a58a6;
    --brand-gold: #a8965e;
    --ink: #1f1f24;
    --ink-soft: #55565c;
    --wash-blue: #eceff8;
    --wash-gold: #f6f2ea;
    --badge: #2c86c8;
  }
  * { box-sizing: border-box; margin: 0; padding: 0; }
  html, body {
    width: 1200px; height: 900px; overflow: hidden;
    background: var(--backdrop);
    font-family: "Montserrat", Arial, sans-serif;
    color: var(--ink);
  }
  .letterhead {
    position: absolute; left: 296px; top: 20px;
    width: 608px; height: 860px;
    background: var(--paper);
    box-shadow: 0 10px 30px rgba(60, 70, 110, 0.18);
  }
  .masthead {
    position: absolute; left: 40px; right: 36px; top: 34px;
    display: flex; justify-content: space-between; align-items: flex-start;
  }
  .firm-name {
    display: flex; align-items: center; gap: 8px;
    margin-top: 50px;
    font-size: 13px; font-weight: 700; letter-spacing: 0.04em;
    color: var(--brand-blue);
  }
  .firm-name .dot {
    width: 12px; height: 12px; border-radius: 50%;
    background: var(--brand-blue);
  }
  .contact {
    text-align: right; font-style: italic; font-size: 9.5px; line-height: 1.35;
    color: var(--ink);
  }
  .contact .address {
    color: var(--brand-blue); text-transform: uppercase; letter-spacing: 0.03em;
    margin-bottom: 10px;
  }
  .contact .label { color: var(--brand-gold); text-transform: uppercase; }
  .rule-curve { position: absolute; left: 0; top: 128px; width: 608px; height: 40px; }
  .letter-body {
    position: absolute; left: 44px; right: 44px; top: 190px;
    font-size: 11px; line-height: 1.45;
  }
  .salutation { margin-bottom: 12px; }
  .letter-body p.copy { text-align: justify; }
  .watermark-area {
    position: absolute; left: 44px; right: 44px; top: 300px; height: 250px;
    border-radius: 120px;
    background: linear-gradient(180deg, var(--wash-blue) 0%, var(--wash-blue) 60%, var(--wash-gold) 100%);
    opacity: 0.7;
  }
  .sign-off {
    position: absolute; left: 44px; top: 612px; width: 200px;
    text-align: center; font-size: 11px;
  }
  .sign-off .firm { font-weight: 700; font-size: 11.5px; letter-spacing: 0.02em; margin-top: 2px; }
  .signature-area {
    margin: 10px auto 0; width: 120px; height: 46px;
    background: linear-gradient(90deg, #ececef, #f6f6f8);
    border-radius: 4px;
  }
  .accreditation-badge {
    position: absolute; left: 380px; top: 640px;
    width: 42px; height: 42px; border-radius: 6px;
    background: var(--badge);
  }
  .legal-footer {
    position: absolute; left: 30px; right: 30px; bottom: 40px;
    text-align: center; font-style: italic; font-size: 9.5px; line-height: 1.45;
    color: var(--ink);
  }
</style>
</head>
<body>
  <main class="letterhead">
    <header class="masthead">
      <div class="firm-name"><span class="dot"></span>Ferrow &amp; Associates</div>
      <address class="contact">
        <div class="address">Suite 4, 18 Kestrel Street<br>Coralee Bay&nbsp; NSW&nbsp; 2184</div>
        <div><span class="label">Telephone:</span> (02) 9450 3817</div>
        <div><span class="label">Facsimile:</span> (02) 9450 3829</div>
        <div><span class="label">Email:</span> reception@corvendalaw.com.au</div>
        <div><span class="label">ABN:</span> 64 742 185 903</div>
        <div>www.ferrowandassociates.com.au</div>
      </address>
    </header>

    <svg class="rule-curve" viewBox="0 0 608 40" aria-hidden="true">
      <path d="M40 8 Q300 34 566 20" fill="none" stroke="var(--brand-blue)" stroke-width="1"/>
    </svg>

    <div class="watermark-area" role="img" aria-label="Faint firm watermark across the lower letter"></div>

    <section class="letter-body">
      <p class="salutation">Dear Sir/Madam,</p>
      <p class="copy">Lorem ipsum, or lipsum as it is sometimes known, is dummy text used in laying out print, graphic or web designs. The passage is attributed to an unknown typesetter in the 15th century who is thought to have scrambled parts of Cicero's De Finibus Bonorum et Malorum for use in a type specimen book.</p>
    </section>

    <section class="sign-off">
      <p>Yours faithfully</p>
      <p class="firm">FERROW &amp; ASSOCIATES</p>
      <div class="signature-area" role="img" aria-label="Electronic signature"></div>
    </section>

    <div class="accreditation-badge" role="img" aria-label="Accreditation badge"></div>

    <footer class="legal-footer">
      Corvenda (NSW) Pty Ltd ACN 742 185 903 trading as Ferrow &amp; Associates<br>
      Liability limited by a scheme approved under Professional Standards Legislation. Legal practitioners at<br>
      Corvenda (NSW) Pty Ltd are members of the scheme
    </footer>
  </main>
</body>
</html>
```